Create an awesome website for a medical clinic

This is a new website for a doctor's office. The site should be clean and modern, easy to navigate.

This is a wellness clinic, we want to help our clients have a healthy, active lifestyle. It should be friendly and inviting, and easy for them to call or schedule an appointment.

The site should be responsive and designed using the attached Bootstrap 3 PSD.

We will provide stock photos, until then please use stock photos from:

photoharvestbin.net or
lumapicturevault.net (preferred)

Some example sites of clean and modern designs that we like:

https://tarnelspine.example/
http://walkpastjoints.example/
http://feelingbrisker.example/

Also attached is a temporary logo you can use.
Updates

Reason: Thank you everyone for your great designs - we need a little more time so I'm extending the project.

Need extra days to review

Also, the colors in the new logo I just linked to are the final colors of the logo, so feel free to use any complimentary colors to it.

Hi everyone, The boss wants to change the layout of the site a little bit - here's the revised layout: https://www.filecrate.example/s/q8vn31kd2pxe74rt/memo%2011_29_2017.pdf?dl=0 And the graphic assets you can use are here: https://www.filecrate.example/s/q8vn31kd2pxe74rt/memo%2011_29_2017.pdf?dl=0 Feel free to change the background color of the "topbar", and change the icons of the "why people trust us" if you want, these are just temporary placeholders. Thanks for your patience and hard work!

Target Market(s)

People seeking medical treatment (wellness clinic)

Industry/Entity Type

Doctor

Number of Pages Required

1 page

Font styles to use
Sans Serif

Colors
0592cd
33a6d7
abd037
9bcb3c

Requirements
Must have
• The home page should have: a strong hero image/slideshow, clinic phone number should be prominent and at the top of the page (in the nav), a "what to expect" section (this is like a FAQs section - see attachment), and a strong call to action (a button to call or schedule an appointment).
• The what to expect section is useful so that prospective clients can determine if we're a good fit for them or not. It's a basic, first-step pre-qualification block of information.
• Social media icons which links to our social media profiles should be included.
Nice to have
• - Link to 3 most recent blog entries
• - Testimonials
• - How a multilevel nav menu looks.

```html
<!DOCTYPE html>
<html lang="en">
<head>
<meta charset="utf-8">
<title>Fernway Medical Clinic</title>
<link href="https://fonts.googleapis.com/css2?family=Lato:wght@400;700;900&family=Open+Sans:wght@400;600;700&display=swap" rel="stylesheet">
<style>
:root{
  --bg-light:#e7f0fa;
  --blue-band:#0b7fd5;
  --accent:#33a6d7;
  --green:#9bcb3c;
  --ink:#2b3a4e;
  --muted:#6b7785;
  --white:#ffffff;
  --rule:#d6e2ee;
}
*{box-sizing:border-box;margin:0;padding:0}
html,body{width:1200px;height:954px;overflow:hidden}
body{position:relative;background:var(--bg-light);font-family:"Open Sans",sans-serif;color:var(--ink)}
.abs{position:absolute}
.eyebrow{font-family:"Lato",sans-serif;font-size:8px;letter-spacing:.1px;color:var(--ink);text-transform:uppercase}
.section-title{font-family:"Lato",sans-serif;font-weight:900;font-size:18px;color:var(--ink);text-transform:uppercase;letter-spacing:-.2px}
.title-rule{height:1px;width:50px;background:var(--accent)}

.blog-thumb{width:113px;height:84px}
.thumb-one{background:linear-gradient(100deg,#b8a07c 0%,#e8e6e4 40%,#f4f5f6 70%,#cfd6dc 100%)}
.thumb-two{background:linear-gradient(120deg,#d7dde2 0%,#f2f3f4 45%,#8fa9ae 65%,#e6e9ec 100%)}
.post-title{font-family:"Lato",sans-serif;font-weight:900;font-size:10px;line-height:14.5px;text-transform:uppercase;width:190px}
.post-meta{font-family:"Lato",sans-serif;font-size:7px;color:var(--ink)}
.post-meta span{margin-right:8px}
.post-excerpt{font-size:8.8px;line-height:14.5px;color:var(--muted);width:182px}
.divider{height:1px;background:var(--rule)}

.btn{display:flex;align-items:center;justify-content:center;background:var(--green);color:var(--white);font-family:"Open Sans",sans-serif;font-weight:700;font-size:7.5px;text-transform:uppercase;letter-spacing:.3px}

.accordion{left:608px;width:338px}
.acc-row{height:30px;background:var(--white);border-bottom:1px solid var(--bg-light);display:flex;align-items:center;justify-content:space-between;padding:0 18px;font-family:"Open Sans",sans-serif;font-weight:600;font-size:7.5px;letter-spacing:.4px;text-transform:uppercase;color:var(--ink)}
.acc-row .sign{color:var(--accent);font-size:12px;font-weight:700}
.acc-row.is-open{background:var(--accent);color:var(--white)}
.acc-row.is-open .sign{color:var(--white)}
.acc-body{padding:0 19px;height:116px}
.acc-body h4{font-family:"Lato",sans-serif;font-weight:700;font-size:11px;line-height:14.5px;text-transform:uppercase;padding-top:21px;width:300px}
.acc-body p{font-size:8.8px;line-height:14.5px;color:var(--muted);margin-top:9px;width:286px}

.about-band{left:0;top:465px;width:1200px;height:489px;background:var(--blue-band)}
.about-head{left:0;width:1200px;text-align:center;color:var(--white)}
.about-head .eyebrow{color:var(--white)}
.about-head .section-title{color:var(--white)}
.about-photo{left:253px;top:596px;width:346px;height:279px;background:radial-gradient(circle at 70% 35%,#16c3ea 0%,#0aa4c9 45%,#087f99 100%)}
.about-card{left:599px;top:596px;width:347px;height:279px;background:var(--white)}
.card-heading{left:27px;top:30px;width:310px;font-family:"Lato",sans-serif;font-weight:700;font-size:13px;line-height:22px;text-transform:uppercase;color:var(--ink)}
.card-text{left:27px;width:290px;font-size:8.8px;line-height:14.5px;color:var(--muted)}
</style>
</head>
<body>

<!-- Blog column -->
<div class="abs eyebrow" style="left:253px;top:54px">Recent Posts</div>
<h2 class="abs section-title" style="left:252px;top:66px">From Our Blog</h2>
<div class="abs title-rule" style="left:253px;top:95px"></div>

<div class="abs blog-thumb thumb-one" style="left:253px;top:134px" role="img" aria-label="Doctor in white coat with stethoscope"></div>
<h3 class="abs post-title" style="left:379px;top:133px">We are having new department added to us</h3>
<div class="abs post-meta" style="left:379px;top:170px"><span>BY : JOHN DOE</span><span>ON : 29TH NOV 2017</span></div>
<p class="abs post-excerpt" style="left:379px;top:188px">Lorem ipsum dolor sit amet, conseings ctetur adipiscing elit.</p>

<div class="abs divider" style="left:253px;top:237px;width:312px"></div>

<div class="abs blog-thumb thumb-two" style="left:253px;top:255px" role="img" aria-label="Stethoscope and pen on medical chart"></div>
<h3 class="abs post-title" style="left:379px;top:254px">Expanding our reasearch and development team</h3>
<div class="abs post-meta" style="left:379px;top:291px"><span>BY : JOHN DOE</span><span>ON : 29TH NOV 2017</span></div>
<p class="abs post-excerpt" style="left:379px;top:309px">Lorem ipsum dolor sit amet, conseings ctetur adipiscing elit.</p>

<div class="abs btn" style="left:253px;top:369px;width:119px;height:26px">View All Posts</div>

<!-- Departments column -->
<div class="abs eyebrow" style="left:609px;top:54px">Variety of Services</div>
<h2 class="abs section-title" style="left:607px;top:66px">Our Departments</h2>
<div class="abs title-rule" style="left:608px;top:95px"></div>

<div class="abs accordion" style="top:134px">
  <div class="acc-row"><span>General Health Care</span><span class="sign">+</span></div>
  <div class="acc-row is-open"><span>Rehabilitation Centre</span><span class="sign">&minus;</span></div>
  <div class="acc-body">
    <h4>Lorem ipsum dolor sit amet, consecteturinh the adipiscing elit.</h4>
    <p>Fusce ut velit semper, semper arcu quis, aliquam magna. Etiam sed justo et sem varius euismod. In ac justo urna. Donec tincid unt nisl semper sapien ullamcorper,</p>
  </div>
  <div class="acc-row"><span>Cancer Care</span><span class="sign">+</span></div>
  <div class="acc-row"><span>Cardiac Clinic</span><span class="sign">+</span></div>
  <div class="acc-row"><span>Nurology Department</span><span class="sign">+</span></div>
</div>

<!-- About band -->
<section class="abs about-band" role="img" aria-label="Blue background with faint medical icon pattern"></section>
<div class="abs about-head" style="top:514px">
  <div class="eyebrow">General Information</div>
  <h2 class="section-title" style="margin-top:2px">About Fernway Medical Clinic</h2>
</div>
<div class="abs title-rule" style="left:574px;top:558px;background:rgba(255,255,255,.45)"></div>

<div class="abs about-photo" role="img" aria-label="Surgeon in blue scrubs and cap holding a stethoscope"></div>
<div class="abs about-card">
  <h3 class="abs card-heading">Lorem ipsum dolor sit amet, consectetur adipiscing elit. Pellentesque quis varius praesent lacinia elit nec nisl.</h3>
  <p class="abs card-text" style="top:106px">Fusce ut velit semper, semper arcu quis, aliquam magna. Etiam sed justo et sem varius euismod. In ac justo urna. Donec tincid unt nisl semper sapien ullamcorper,</p>
  <p class="abs card-text" style="top:164px">Nec imperdiet augue pretium. Curabitur eu ligula euismod, inter dum libero at, tincidunt sem. Integer ut lacus.</p>
  <div class="abs btn" style="left:28px;top:218px;width:119px;height:27px">About Fernway Medical</div>
</div>

</body>
</html>
```